Presentation Folder Design for Photographer

Professional photographer requires a presentation folder for marketing.
I specialise in architecture, corporate & commercial photography. The folder will be used to promote my architectural photography services to real estate, accomodation & architect clients.

I'm looking for a modern clean design that complements my logo with complimentary text & colours. I want to use some images in the design, probably a mix of images not just architectural. I need a print ready design in PDF as well as a PSD file that I can possibly edit / update images later on.

The folder will be a double sided design with no need for pockets included in the design. Overall dimensions are 430mm ( folded down the centre ) x 315mm with a 5mm trim & bleed.

The layout would be as follows :

Front cover - Logo + maybe some images or some other design work.

Inside front cover - Some text about my services.

ARCHITECTURE
Commercial Residential Real Estate Drone Floorpans Accommodation

CORPORATE
Studio Headshots Environmental Portraits Staff Photography

COMMERCIAL
Product Advertising Fashion Event Stock

Inside back cover - no text as a seperate price list will sit here.

Outside back cover - I was thinking of having a collage of images worked into
the design but open to the designers input as well.
I also have another logo with phone number & web address
I would like on the back cover - Will be included in the files
provided.

I have a black background & white background version of my logo I will include both for the design work. I'm trying to get away from an all black design so if using the black logo I don't want a completely black page design, just becomes to heavy.

I'm redoing my website soon so please base the folder design around my logo text & colours not my current website as it's very outdated.

Logo brand guide is as follows

Main Font Font: Reislust
Main Font Color: #fff
Slogan Font Font: Ubuntu Bold
Monogram Font Font: Venti Medium
Container Color: #fff

Please respect the copyright on the images provided and delete all content once the design has been completed.
Thanks.

Need extra days to review

```html
<!DOCTYPE html>
<html lang="en">
<head>
<meta charset="utf-8">
<title>Lumen Frame – Presentation Folder</title>
<link rel="stylesheet" href="https://fonts.googleapis.com/css2?family=Montserrat:wght@300;400;600&display=swap">
<style>
  :root {
    --page-bg: #e3e1e2;
    --ink: #232323;
    --band-dark: #0b0b0b;
    --panel-dark: #222222;
    --gold: #c9a24a;
    --gold-text: #b5822c;
    --white: #ffffff;
    --label: #2c2c2c;
  }
  * { box-sizing: border-box; margin: 0; padding: 0; }
  html, body { width: 979px; height: 1200px; overflow: hidden; }
  body {
    position: relative;
    background: var(--page-bg);
    font-family: "Montserrat", Arial, sans-serif;
  }
  .spread {
    position: absolute;
    left: 134px;
    width: 688px;
    height: 462px;
    box-shadow: 0 3px 6px rgba(0,0,0,0.35);
    overflow: hidden;
  }
  .spread-outside { top: 92px; background: var(--panel-dark); }
  .spread-inside { top: 636px; background: var(--white); }
  .spread-label {
    position: absolute;
    left: 0; width: 979px;
    text-align: center;
    font-weight: 300;
    font-size: 24px;
    letter-spacing: 3px;
    color: var(--label);
  }
  .label-outside { top: 578px; }
  .label-inside { top: 1133px; }

  .brand {
    position: absolute;
    display: flex;
    align-items: center;
    gap: 10px;
    color: var(--white);
    font-weight: 400;
    text-transform: uppercase;
    white-space: nowrap;
  }
  .brand-mark {
    border: 2px solid var(--gold);
    border-radius: 3px;
  }
  .brand-small { left: 102px; top: 60px; font-size: 9px; letter-spacing: 2px; }
  .brand-small .brand-mark { width: 24px; height: 24px; }
  .brand-large { left: 402px; top: 42px; font-size: 15px; letter-spacing: 3.5px; }
  .brand-large .brand-mark { width: 44px; height: 44px; }
  .brand-inside { left: 57px; top: 362px; font-size: 13px; letter-spacing: 3px; }
  .brand-inside .brand-mark { width: 40px; height: 40px; }

  .photo { position: absolute; }
  .contact-band {
    position: absolute;
    left: 0; top: 430px; width: 688px; height: 32px;
    background: var(--band-dark);
    color: var(--gold);
  }
  .contact-web { position: absolute; left: 106px; top: 9px; font-size: 10px; }
  .contact-phone { position: absolute; left: 484px; top: 6px; font-size: 13px; letter-spacing: 2.5px; }

  .services-panel { position: absolute; left: 0; top: 0; width: 345px; height: 318px; background: var(--white); }
  .gallery-panel {
    position: absolute; left: 345px; top: 0; width: 343px; height: 318px;
    background: linear-gradient(90deg, #f0f0f0 0%, #ffffff 30%);
  }
  .service { position: absolute; left: 28px; }
  .service-title {
    color: var(--gold-text);
    font-weight: 600;
    font-size: 13px;
    letter-spacing: 0.3px;
    margin-bottom: 7px;
  }
  .service-list { color: var(--ink); font-size: 12.3px; line-height: 15px; }
  .service-architecture { top: 37px; }
  .service-corporate { top: 114px; }
  .service-commercial { top: 182px; }

  .inside-band {
    position: absolute; left: 0; top: 318px; width: 688px; height: 144px;
    background: var(--panel-dark);
  }
  .card-slot {
    position: absolute; left: 470px; top: 28px; width: 132px; height: 90px;
    background: var(--white);
    display: flex; align-items: center; justify-content: center;
    text-align: center;
    font-size: 11.5px; line-height: 16px; color: var(--ink);
  }
  .card-slot svg { position: absolute; left: 0; top: 0; }
</style>
</head>
<body>

<section class="spread spread-outside" aria-label="Folder outside">
  <div class="brand brand-small"><span class="brand-mark"></span>Lumen Frame</div>
  <div class="brand brand-large"><span class="brand-mark"></span>Lumen Frame</div>

  <div class="photo" style="left:0;top:123px;width:109px;height:168px;background:linear-gradient(135deg,#e9e5df,#8a6a4c);" role="img" aria-label="White kitchen island with framed pictures on the wall"></div>
  <div class="photo" style="left:112px;top:123px;width:150px;height:168px;background:linear-gradient(180deg,#a77aa0 0%,#d69a6c 45%,#4a3a30 100%);" role="img" aria-label="Blue classic car in front of a shed at dusk"></div>
  <div class="photo" style="left:266px;top:123px;width:137px;height:306px;background:linear-gradient(180deg,#d9c8b4 0%,#c9a68a 55%,#ece7e2 80%,#c8a58f 100%);" role="img" aria-label="Bedroom with chandelier and a gallery wall of frames"></div>
  <div class="photo" style="left:406px;top:123px;width:150px;height:168px;background:linear-gradient(180deg,#eeeeec,#5a5550);" role="img" aria-label="Bright kitchen with bar stools"></div>
  <div class="photo" style="left:558px;top:123px;width:130px;height:168px;background:linear-gradient(160deg,#d8cfc6 0%,#6f7a5a 45%,#a05a30 100%);" role="img" aria-label="Open living room with timber floor and garden windows"></div>

  <div class="photo" style="left:0;top:294px;width:70px;height:135px;background:linear-gradient(180deg,#6d6d6d,#e9e9e9);" role="img" aria-label="Modern bathroom with white basin"></div>
  <div class="photo" style="left:74px;top:294px;width:91px;height:135px;background:linear-gradient(180deg,#3a4f96 0%,#6c6a80 55%,#4d5a2a 100%);" role="img" aria-label="Heritage house at twilight"></div>
  <div class="photo" style="left:168px;top:294px;width:93px;height:135px;background:linear-gradient(180deg,#e6ddd0,#b59e86);" role="img" aria-label="Kitchen with stone feature bench"></div>
  <div class="photo" style="left:406px;top:294px;width:95px;height:135px;background:linear-gradient(180deg,#e9e9e9 0%,#4c4c4c 55%,#c9b54a 100%);" role="img" aria-label="Kitchen with yellow stools"></div>
  <div class="photo" style="left:504px;top:294px;width:92px;height:135px;background:linear-gradient(180deg,#4c6aa8 0%,#8b8d90 50%,#5a6a3a 100%);" role="img" aria-label="Modern two-storey townhouse"></div>
  <div class="photo" style="left:599px;top:294px;width:89px;height:135px;background:linear-gradient(180deg,#5d88c8 0%,#b9c1cc 55%,#4a4a4a 100%);" role="img" aria-label="Angular contemporary building facade"></div>

  <div class="contact-band">
    <span class="contact-web">www.lumenframe.com.au</span>
    <span class="contact-phone">0400 555 018</span>
  </div>
</section>
<div class="spread-label label-outside">OUTSIDE</div>

<section class="spread spread-inside" aria-label="Folder inside">
  <div class="services-panel">
    <div class="service service-architecture">
      <h2 class="service-title">ARCHITECTURE</h2>
      <p class="service-list">Commercial Residential Real Estate Drone<br>Floorpans Accommodation</p>
    </div>
    <div class="service service-corporate">
      <h2 class="service-title">CORPORATE</h2>
      <p class="service-list">Studio Headshots Environmental Portraits<br>Staff Photography</p>
    </div>
    <div class="service service-commercial">
      <h2 class="service-title">COMMERCIAL</h2>
      <p class="service-list">Product Advertising Fashion Event Stock</p>
    </div>
  </div>

  <div class="gallery-panel">
    <div class="photo" style="left:33px;top:38px;width:90px;height:125px;background:linear-gradient(180deg,#6a5a68 0%,#4e7ab0 45%,#6a4a2a 100%);" role="img" aria-label="Fashion portrait in a garden"></div>
    <div class="photo" style="left:33px;top:168px;width:90px;height:57px;background:linear-gradient(180deg,#f2f2f2,#5a5a5a);" role="img" aria-label="Minimal white kitchen"></div>
    <div class="photo" style="left:127px;top:38px;width:90px;height:186px;background:linear-gradient(180deg,#b8a27e 0%,#8a7a62 50%,#3a3a3a 100%);" role="img" aria-label="Fashion shoot at a stone doorway with balloons"></div>
    <div class="photo" style="left:222px;top:38px;width:90px;height:58px;background:linear-gradient(180deg,#1a1a1a,#8a8a8a);" role="img" aria-label="Product shot of a wristwatch"></div>
    <div class="photo" style="left:222px;top:102px;width:90px;height:123px;background:linear-gradient(135deg,#e9e5df,#6a4a30);" role="img" aria-label="White kitchen island with framed pictures"></div>
  </div>

  <div class="inside-band">
    <div class="brand brand-inside"><span class="brand-mark"></span>Lumen Frame</div>
    <div class="card-slot">
      <svg width="132" height="90" viewBox="0 0 132 90" aria-hidden="true">
        <polygon points="0,0 16,0 0,12" fill="#111"/>
        <polygon points="132,0 116,0 132,12" fill="#111"/>
        <polygon points="0,90 16,90 0,78" fill="#111"/>
        <polygon points="132,90 116,90 132,78" fill="#111"/>
      </svg>
      <span>Space for<br>Business card</span>
    </div>
  </div>
</section>
<div class="spread-label label-inside">INSIDE</div>

</body>
</html>
```